Business Card/ Sign Modern Design for Real Estate Brokerage & Property Management company
Verlan Realty & Property Management If it's Real Estate, We've got you covered!
Business Card/ Sign Modern Design for Real Estate Brokerage & Property Management company - Real Estate
Creative Brief
Use specific fonts
Any sleek, easy to read font
Modern
Dennis Kowalcik
Owner/Broker
847 e 19th Street suite 410 Kansas City, MO 64127
den@verlanHQ.com
www.verlanHQ.com
Licensed in KS & MO
Our colors are grey & orange. Looking for something fresh & current. Please leave room on front of card for personal photo. We are a Real Estate & Property Management company. Our slogan is: If it's real estate, we've got you covered!
Whatever Design is on the back of the business card will most likely be the design we use for our yard signs & window decals also.
mossle mossle
Please leave room for a personal photo in your design submissions. I've uploaded a jpeg of the photo we will use
#35 & #36 really like the back of these cards! Any way to add our full name "Verlan Realty & Property Management"
Thank you for the great submissions! We are really liking the ones that focus more on the grey color with pops of orange. Is there any way to submit designs that will allow room for a picture? Would it help if we upload the personal photo that will be used? #31 instead of black, can you use a dark grey on the back of this card? Also, underneath the shield logo can you add "Verlan Realty & Property Management"
Uploaded EPS & PDF file Thanks!

```html
<!DOCTYPE html>
<html lang="en">
<head>
<meta charset="utf-8">
<title>Verlan Realty – Stationery Set</title>
<link href="https://fonts.googleapis.com/css2?family=Montserrat:wght@400;600;700&display=swap" rel="stylesheet">
<style>
:root{
  --bg:#2b2b2b;
  --orange:#f26b1d;
  --orange-dark:#d9530c;
  --grey:#3a3a3a;
  --photo:#8a8a8a;
  --paper:#ffffff;
  --ink:#555555;
  --label:#9a9a9a;
}
*{box-sizing:border-box;margin:0;padding:0}
html,body{width:1200px;height:247px;overflow:hidden}
body{
  position:relative;
  font-family:'Montserrat',sans-serif;
  background:var(--bg);
}
.item{position:absolute;box-shadow:0 1px 4px rgba(0,0,0,.6)}
.label{position:absolute;font-size:4px;color:var(--label);letter-spacing:.2px;white-space:nowrap}
.brand{font-weight:700;letter-spacing:.6px;display:flex;align-items:center;gap:3px;white-space:nowrap}
.brand .dot{border-radius:50%;background:var(--orange);display:inline-block;flex:none}

.logo-mark{position:absolute;left:67px;top:14px;width:78px;height:58px;display:flex;flex-direction:column;align-items:center;justify-content:center;color:#fff}
.logo-mark .brand{font-size:13px}
.logo-mark .brand .dot{width:9px;height:9px}
.logo-mark .sub{font-size:3.6px;color:#cfcfcf;margin-top:3px;text-align:center}

.card{width:48px;height:34px;padding:3px}
.card--front{display:flex;align-items:center;gap:3px}
.card--front.is-orange{background:var(--orange);color:#fff}
.card--front.is-orange .brand .dot{background:#fff}
.card--front.is-white{background:var(--paper);color:var(--grey)}
.card .photo{flex:none;width:15px;height:20px;background:linear-gradient(180deg,#a3a3a3,var(--photo));border:1px solid rgba(255,255,255,.7)}
.card--front .text{display:flex;flex-direction:column;min-width:0}
.card--front .brand{font-size:4.6px;gap:1.5px;letter-spacing:.3px}
.card--front .brand .dot{width:3.2px;height:3.2px}
.card--front .slogan{font-size:1.9px;line-height:1.3;margin-top:1.5px}
.card--back{background:var(--paper);color:var(--ink);font-size:2.3px;line-height:1.35;border-left:2px solid var(--orange);display:flex;flex-direction:column;justify-content:center;padding:3px 4px}
.card--back .name{font-weight:700;font-size:3.2px;color:var(--grey)}
.card--back .role{color:var(--orange)}

.letterhead{width:106px;height:223px;background:var(--paper);padding:12px 10px;color:var(--ink);font-size:3.2px;line-height:1.5}
.letterhead::before{content:"";position:absolute;right:0;top:0;width:32px;height:6px;background:var(--orange)}
.letterhead .head{display:flex;flex-direction:column;align-items:center;color:var(--grey);margin-bottom:14px}
.letterhead .head .brand{font-size:8px}
.letterhead .head .brand .dot{width:5px;height:5px}
.letterhead .head .sub{font-size:2.4px;margin-top:1px}
.letterhead p{margin-bottom:4px}
.letterhead .sign{margin-top:48px;font-weight:600;color:var(--grey)}
.letterhead .foot{position:absolute;left:0;right:0;bottom:0;height:16px;background:linear-gradient(90deg,var(--orange),var(--orange-dark));color:#fff;font-size:2.4px;display:flex;align-items:center;justify-content:center;gap:4px}

.slip{left:403px;top:149px;width:72px;height:48px;background:var(--paper);border-top:5px solid var(--orange);display:flex;align-items:center;justify-content:center;color:var(--grey)}
.slip .brand{font-size:7px}
.slip .brand .dot{width:5px;height:5px}

.envelope{width:108px;height:54px;background:var(--paper);overflow:hidden}
.envelope svg{position:absolute;left:0;top:0}
.envelope .brand{position:absolute;left:6px;bottom:6px;font-size:5px;color:var(--grey)}
.envelope .brand .dot{width:4px;height:4px}

.folder-back{left:600px;top:36px;width:96px;height:192px;background:var(--grey)}
.folder-back .pocket{position:absolute;left:0;right:0;bottom:0;height:80px;background:var(--orange)}
.folder-front{left:696px;top:29px;width:96px;height:204px;background:linear-gradient(160deg,var(--orange),var(--orange-dark));display:flex;flex-direction:column;align-items:center;justify-content:center;color:#fff}
.folder-front .brand{font-size:12px}
.folder-front .brand .dot{width:8px;height:8px;background:#fff}
.folder-front .sub{font-size:3px;margin-top:3px}
</style>
</head>
<body>

<div class="logo-mark">
  <div class="brand"><span class="dot"></span>VERLAN</div>
  <div class="sub">Verlan Realty &amp; Property Management</div>
</div>
<div class="label" style="left:88px;top:76px">Logo Design</div>

<div class="item card card--front is-orange" style="left:7px;top:98px">
  <div class="photo" role="img" aria-label="Space for the broker's personal photo"></div>
  <div class="text">
    <div class="brand"><span class="dot"></span>VERLAN</div>
    <div class="slogan">If it's real estate, we've got you covered!</div>
  </div>
</div>
<div class="item card card--back" style="left:60px;top:98px">
  <div class="name">Dennis Kowalcik</div>
  <div class="role">Owner/Broker</div>
  <div>847 e 19th Street suite 410</div>
  <div>Kansas City, MO 64127</div>
  <div>den@verlanHQ.com</div>
  <div>www.verlanHQ.com</div>
</div>
<div class="item card card--front is-white" style="left:7px;top:144px">
  <div class="photo" role="img" aria-label="Space for the broker's personal photo"></div>
  <div class="text">
    <div class="brand"><span class="dot"></span>VERLAN</div>
    <div class="slogan">If it's real estate, we've got you covered!</div>
  </div>
</div>
<div class="item card card--back" style="left:60px;top:144px">
  <div class="name">Dennis Kowalcik</div>
  <div class="role">Licensed in KS &amp; MO</div>
  <div>den@verlanHQ.com</div>
  <div>www.verlanHQ.com</div>
</div>
<div class="label" style="left:40px;top:184px">Business Card</div>

<div class="item letterhead" style="left:158px;top:12px">
  <div class="head"><div class="brand"><span class="dot"></span>VERLAN</div><div class="sub">Verlan Realty &amp; Property Management</div></div>
  <p>Dear Client,</p>
  <p>Thank you for choosing us to manage your property.</p>
  <p>We look forward to working with you.</p>
  <p>Sincerely,</p>
  <div class="sign">Dennis Kowalcik</div>
  <div class="foot"><span>den@verlanHQ.com</span><span>www.verlanHQ.com</span></div>
</div>
<div class="label" style="left:198px;top:238px">Letterhead</div>

<div class="item letterhead" style="left:278px;top:12px">
  <div class="head"><div class="brand"><span class="dot"></span>VERLAN</div><div class="sub">Verlan Realty &amp; Property Management</div></div>
  <p>Dear Client,</p>
  <p>Thank you for choosing us to manage your property.</p>
  <p>We look forward to working with you.</p>
  <p>Sincerely,</p>
  <div class="sign">Dennis Kowalcik</div>
  <div class="foot"><span>den@verlanHQ.com</span><span>www.verlanHQ.com</span></div>
</div>
<div class="label" style="left:318px;top:238px">Letterhead</div>

<div class="item slip">
  <div class="brand"><span class="dot"></span>VERLAN</div>
</div>
<div class="label" style="left:420px;top:201px">Compliment Slip</div>

<div class="item envelope" style="left:480px;top:115px">
  <svg width="108" height="54" viewBox="0 0 108 54"><path d="M0 0H108L54 22Z" fill="var(--orange)"/></svg>
  <div class="brand"><span class="dot"></span>VERLAN</div>
</div>
<div class="item envelope" style="left:480px;top:180px">
  <svg width="108" height="54" viewBox="0 0 108 54"><rect width="108" height="4" fill="var(--orange)"/></svg>
  <div class="brand"><span class="dot"></span>VERLAN</div>
</div>
<div class="label" style="left:524px;top:238px">Envelope</div>

<div class="item folder-back"><div class="pocket"></div></div>
<div class="item folder-front">
  <div class="brand"><span class="dot"></span>VERLAN</div>
  <div class="sub">Verlan Realty &amp; Property Management</div>
</div>
<div class="label" style="left:686px;top:238px">Folder</div>

</body>
</html>
```